Residential & commercial landscaping company

Updated business cards for commercial and landscaping company. We would like to keep out logo, but just need a more updated business card.

```html
<!DOCTYPE html>
<html lang="en">
<head>
<meta charset="utf-8">
<title>Verdant Ridge – Business Card</title>
<link href="https://fonts.googleapis.com/css2?family=Montserrat:wght@400;500;600;700;800&family=Open+Sans:wght@600&display=swap" rel="stylesheet">
<style>
  :root {
    --bg: #161616;
    --lime: #8cd33f;
    --leaf: #77bb3a;
    --forest: #4f7a22;
    --deep: #3c6a1a;
    --pine: #0f6a3a;
    --ink: #231f20;
    --charcoal: #2a2a2a;
    --paper: #f7f7f5;
    --label: #8cd33f;
  }
  * { box-sizing: border-box; margin: 0; padding: 0; }
  html, body { width: 1200px; height: 1200px; overflow: hidden; background: var(--bg); }
  body { position: relative; font-family: "Montserrat", sans-serif; }

  .sheet-label {
    position: absolute; left: 80px; top: 70px;
    color: var(--label); font-family: "Open Sans", sans-serif; font-weight: 600;
    font-size: 30px; line-height: 1.35;
  }

  .card {
    position: absolute; width: 520px; height: 320px;
    background: var(--paper); overflow: hidden;
    box-shadow: 0 18px 40px rgba(0,0,0,.55);
  }
  .card > svg { position: absolute; inset: 0; width: 100%; height: 100%; }
  .card--front { left: 600px; top: 250px; }
  .card--back  { left: 80px;  top: 650px; }

  .brand {
    position: absolute; display: flex; align-items: center; gap: 10px;
    font-weight: 800; color: var(--ink); letter-spacing: -0.5px; white-space: nowrap;
  }
  .brand__mark { width: 26px; height: 26px; background: var(--leaf); flex: none; }
  .card--front .brand { left: 60px; top: 62px; font-size: 34px; }
  .card--back .brand { right: 40px; bottom: 28px; font-size: 28px; }
  .card--back .brand .brand__mark { width: 22px; height: 22px; }

  .contact { position: absolute; left: 262px; top: 70px; color: var(--ink); white-space: nowrap; }
  .contact__name { font-size: 22px; font-weight: 500; color: var(--lime); letter-spacing: .3px; }
  .contact__name b { font-weight: 700; }
  .contact__role { font-size: 10px; font-weight: 700; margin-top: 2px; }
  .contact__lines { margin-top: 26px; font-size: 10.5px; line-height: 1.55; }
  .contact__lines + .contact__lines { margin-top: 14px; }
  .accent { color: var(--lime); }

  .badge {
    position: absolute; width: 30px; height: 30px; border-radius: 50%;
    background: var(--leaf); border: 3px solid #fff;
    box-shadow: 0 0 0 2px var(--leaf);
    display: flex; align-items: center; justify-content: center;
  }
  .badge svg { width: 14px; height: 14px; }
  .badge--mail { left: 218px; top: 136px; }
  .badge--phone { left: 204px; top: 190px; }
</style>
</head>
<body>

<div class="sheet-label">Business Card - Mockup1<br>Size: 3.25 in(W) X 2.00 in(H)</div>

<section class="card card--front">
  <svg viewBox="0 0 520 320" preserveAspectRatio="none" aria-hidden="true">
    <rect width="520" height="320" fill="var(--paper)"/>
    <path d="M0,95 C70,120 120,230 290,240 C390,246 460,238 520,236 L520,320 L0,320 Z" fill="var(--lime)"/>
    <path d="M0,175 C110,220 230,290 520,300 L520,320 L0,320 Z" fill="var(--charcoal)"/>
    <path d="M0,132 C90,165 170,225 320,238 C420,246 480,270 520,305" fill="none" stroke="var(--ink)" stroke-width="16"/>
    <path d="M0,150 C60,190 140,280 330,292 C420,298 480,306 520,312" fill="none" stroke="var(--forest)" stroke-width="2.5"/>
    <path d="M0,118 C90,160 200,190 330,240 C400,268 450,290 470,320" fill="none" stroke="var(--forest)" stroke-width="2.5"/>
    <path d="M0,200 C120,245 260,290 520,296" fill="none" stroke="var(--lime)" stroke-width="2"/>
  </svg>
  <div class="brand"><span class="brand__mark"></span>Verdant Ridge</div>
</section>

<section class="card card--back">
  <svg viewBox="0 0 520 320" preserveAspectRatio="none">
    <rect width="520" height="320" fill="var(--paper)"/>
    <path d="M0,0 L300,0 C250,80 240,190 0,250 Z" fill="var(--leaf)"/>
    <path d="M0,0 L250,0 C205,90 170,160 0,230 Z" fill="var(--deep)" role="img" aria-label="Tree illustration on layered green hills"/>
    <path d="M0,260 C120,240 180,170 230,110" fill="none" stroke="var(--lime)" stroke-width="2"/>
    <path d="M28,230 C40,175 120,170 170,150 C200,138 215,120 230,100" fill="none" stroke="#fff" stroke-width="12"/>
    <path d="M20,235 C20,170 110,160 160,138 C190,124 205,100 215,60" fill="none" stroke="var(--pine)" stroke-width="3"/>
    <path d="M0,255 C120,265 210,230 240,170 L245,100" fill="none" stroke="var(--leaf)" stroke-width="2.5"/>
  </svg>

  <div class="badge badge--mail">
    <svg viewBox="0 0 16 16" aria-hidden="true"><path d="M1,4 H15 V12 H1 Z M1,4 L8,9 L15,4" fill="#fff" stroke="var(--leaf)" stroke-width="1"/></svg>
  </div>
  <div class="badge badge--phone">
    <svg viewBox="0 0 16 16" aria-hidden="true"><path d="M4,1 C2,2 1,4 2,7 C4,11 7,14 11,15 C13,15 14,14 15,12 L12,9 L10,11 C8,10 6,8 5,6 L7,4 Z" fill="#fff"/></svg>
  </div>

  <div class="contact">
    <p class="contact__name"><b>Daniel</b> Harlow Jr.</p>
    <p class="contact__role">Project Manager</p>
    <div class="contact__lines">
      <p>dan@VerdantRidgeLandscape.com</p>
      <p>www.VerdantRidgeLandscape.com</p>
    </div>
    <div class="contact__lines">
      <p><span class="accent">P:</span>555-01-4836 <span class="accent">ext.</span> 417</p>
      <p><span class="accent">F:</span> 555-010-9362</p>
    </div>
  </div>

  <div class="brand"><span class="brand__mark"></span>Verdant Ridge</div>
</section>

</body>
</html>
```